Corporate-Design für Zahnarztpraxis
Zielgruppe
Ich bin Zahnärztin in einer Einzelbehandler Praxis. Die Praxis liegt im ländlichen Gebiet am Rand von Berlin. Zielgruppe sind neue Patienten jeglichen Alters. Die Praxis zeichnet sich durch eine familiäre vertrauenesvolle Atmosphäre im Umgang mit den Patienten aus.
Aufgabenstellung
- weibliches Erscheinungsbild
- warme Farben
- Vertrauen
- bei Verwendung eines Zahns als Symbols sollte dieser indirekt dargestellt werden, eventuell die Form eines Zahnes aufgreifen

```html
<!DOCTYPE html>
<html lang="de">
<head>
<meta charset="utf-8">
<title>Zahnarztpraxis Clara Wendt – Visitenkarten</title>
<link href="https://fonts.googleapis.com/css2?family=Maven+Pro:wght@400&display=swap" rel="stylesheet">
<style>
  :root {
    --orange: #f08145;
    --grey: #8a8a8a;
    --name-grey: #7d7d7d;
    --white: #ffffff;
    --page: #fdfdfd;
  }
  * { margin: 0; padding: 0; box-sizing: border-box; }
  html, body { width: 1200px; height: 991px; overflow: hidden; background: var(--page); }
  body { position: relative; font-family: "Maven Pro", "Trebuchet MS", sans-serif; color: var(--white); }

  .card {
    position: absolute; top: 167px; width: 415px; height: 640px;
    box-shadow: 14px 10px 18px rgba(0,0,0,0.12);
  }
  .card--front { left: 137px; background: var(--white); }
  .card--back { left: 630px; background: var(--grey); }

  .brand-mark {
    position: absolute; left: 45px; top: 116px;
    width: 70px; height: 70px; border-radius: 50%;
  }
  .card--front .brand-mark { background: var(--orange); }
  .card--back .brand-mark { background: var(--white); }

  .brand {
    position: absolute; left: 133px; top: 112px;
    font-weight: 400; text-transform: uppercase; line-height: 1.1;
  }
  .brand__kind { display: block; font-size: 23px; color: var(--orange); }
  .brand__name { display: block; font-size: 28px; margin-top: 4px; }
  .card--front .brand__name { color: var(--name-grey); }
  .card--back .brand__name { color: var(--white); }

  .info {
    position: absolute; left: 0; right: 0; top: 331px; bottom: 0;
    background: var(--orange);
  }
  .info__line { position: absolute; left: 0; right: 0; text-align: center; }
  .info__address { top: 13px; font-size: 25px; }
  .info__title { top: 14px; font-size: 23.5px; }
  .info__web { top: 233px; font-size: 22px; }

  .contact { position: absolute; left: 60px; top: 89px; font-size: 23px; line-height: 29px; }
  .contact__row { display: flex; }
  .contact__label { width: 93px; }
  .contact__mail { font-size: 21px; letter-spacing: 0.6px; }

  .hours { position: absolute; left: 0; right: 12px; top: 89px; text-align: center; font-size: 24px; line-height: 29px; }
</style>
</head>
<body>
  <section class="card card--front">
    <div class="brand-mark" role="img" aria-label="Platz für das Praxiszeichen"></div>
    <div class="brand">
      <span class="brand__kind">Zahnarztpraxis</span>
      <span class="brand__name">Clara Wendt</span>
    </div>
    <div class="info">
      <p class="info__line info__address">Lindenweg 8 | 15366 Birkenfelde</p>
      <div class="contact">
        <div class="contact__row"><span class="contact__label">Telefon</span><span>+43 5523 47 218 60</span></div>
        <div class="contact__row"><span class="contact__label">Mobil</span><span>+43 664 2873 415</span></div>
        <div class="contact__mail">praxis@clara-wendt.de</div>
      </div>
      <p class="info__line info__web">www.zahnarztpraxis-wendt.de</p>
    </div>
  </section>

  <section class="card card--back">
    <div class="brand-mark" role="img" aria-label="Platz für das Praxiszeichen"></div>
    <div class="brand">
      <span class="brand__kind">Zahnarztpraxis</span>
      <span class="brand__name">Clara Wendt</span>
    </div>
    <div class="info">
      <p class="info__line info__title">Öffnungszeiten</p>
      <div class="hours">
        <p>Montag bis Freitag</p>
        <p>9.00 Uhr bis 17.00 Uhr</p>
        <p>sowie nach Vereinbarung</p>
      </div>
      <p class="info__line info__web">www.zahnarztpraxis-wendt.de</p>
    </div>
  </section>
</body>
</html>
```